Youtube Thumbnail templates x 4 for football channel (more than 1 winner will be chosen)

I am looking for a set of 4 thumbnail templates that are on brand.

They should be eye catching and baiting the click.

The 4 different thumbnails will likely be very similar.

It is highly likely that I will choose more than 1 designer as the winner for the project

I have added my brand guidelines below as well as my logo.

The website page to get a good feel for my brand is: https://bravolane.global/474-mentoring/

Also, please feel free to add any images of famous footballers in the template, as these will be delivered in PSD file at the end I will be able to edit these thumbnails before they go live

Football players of all levels

Sans Serif

• Be on brand.
Be eye catching and very clickable

```html
<!DOCTYPE html>
<html lang="en">
<head>
<meta charset="utf-8">
<title>Football Thumbnail Templates</title>
<link rel="stylesheet" href="https://fonts.googleapis.com/css2?family=Archivo+Black&family=Montserrat:wght@700&display=swap">
<style>
  :root {
    --page-bg: #1a1a1b;
    --blue-light: #2aa3e6;
    --blue-mid: #1672b8;
    --blue-deep: #0b3f78;
    --paper: #d9d9d6;
    --paper-dark: #b7b7b4;
    --ink: #0a1622;
    --glow: #48d4ff;
    --white: #ffffff;
    --thumb-w: 515px;
    --thumb-h: 290px;
  }
  * { box-sizing: border-box; margin: 0; padding: 0; }
  html, body { width: 675px; height: 1200px; overflow: hidden; }
  body {
    background: radial-gradient(ellipse at 30% 20%, #2a2a2b 0%, var(--page-bg) 60%, #101011 100%);
    font-family: "Montserrat", sans-serif;
    position: relative;
  }
  .thumbnail {
    position: absolute;
    left: 80px;
    width: var(--thumb-w);
    height: var(--thumb-h);
    overflow: hidden;
    background: radial-gradient(ellipse at 45% 40%, var(--blue-light) 0%, var(--blue-mid) 50%, var(--blue-deep) 100%);
  }
  .thumbnail--one   { top: 8px; }
  .thumbnail--two   { top: 305px; }
  .thumbnail--three { top: 604px; }
  .thumbnail--four  { top: 902px; }

  .headline {
    position: absolute;
    color: var(--white);
    font-family: "Archivo Black", sans-serif;
    font-weight: 400;
    font-size: 44px;
    line-height: 56px;
    letter-spacing: 0;
    text-transform: uppercase;
    -webkit-text-stroke: 7px var(--ink);
    paint-order: stroke fill;
    text-shadow: 0 0 4px var(--glow), 0 0 2px var(--glow);
    white-space: nowrap;
    z-index: 3;
  }
  .headline span { display: block; }

  .photo { position: absolute; }
  .paper-strip {
    position: absolute;
    background: linear-gradient(160deg, var(--paper) 0%, var(--paper-dark) 100%);
  }

  .brand {
    position: absolute;
    display: flex;
    align-items: center;
    gap: 5px;
    width: 96px;
    color: var(--white);
    font-weight: 700;
    font-size: 11px;
    line-height: 1;
    letter-spacing: 0.3px;
    z-index: 4;
  }
  .brand__dot {
    width: 16px; height: 16px;
    border-radius: 50%;
    border: 1.5px solid currentColor;
    flex: none;
  }
  .brand--vertical { transform: rotate(-90deg); transform-origin: center; }
  .brand--dark { color: var(--ink); }

  /* Thumbnail one */
  .thumbnail--one .paper-strip {
    left: 0; top: 0; width: 60px; height: 100%;
    clip-path: polygon(0 0, 92% 0, 100% 8%, 94% 20%, 99% 34%, 93% 49%, 100% 62%, 94% 78%, 99% 90%, 95% 100%, 0 100%);
  }
  .thumbnail--one .brand { left: -22px; top: 128px; }
  .thumbnail--one .headline { left: 76px; top: 30px; }
  .thumbnail--one .photo {
    right: 0; top: 0; width: 190px; height: 100%;
    background: linear-gradient(180deg, #6b6b6b 0%, #2c2c2c 45%, #9a9a9a 100%);
    clip-path: polygon(18% 0, 100% 0, 100% 100%, 0 100%, 12% 70%, 10% 40%);
  }

  /* Thumbnail two */
  .thumbnail--two .photo {
    left: 0; top: 0; width: 265px; height: 100%;
    background: linear-gradient(135deg, #c9c6bf 0%, #7a6650 45%, #3b2a18 100%);
    clip-path: polygon(0 0, 94% 0, 98% 14%, 93% 30%, 100% 48%, 94% 64%, 99% 80%, 93% 100%, 0 100%);
  }
  .thumbnail--two .brand { left: 12px; top: 252px; }
  .thumbnail--two .headline { right: 25px; top: 32px; text-align: right; }

  /* Thumbnail three */
  .thumbnail--three .photo {
    left: 0; top: 112px; width: 100%; height: 178px;
    background: linear-gradient(180deg, #1d1a12 0%, #6b5317 50%, #c9a122 100%);
    clip-path: polygon(0 4%, 12% 1%, 25% 5%, 40% 0, 55% 4%, 70% 1%, 85% 5%, 100% 2%, 100% 100%, 0 100%);
  }
  .thumbnail--three .headline { left: 0; right: 0; top: 14px; text-align: center; line-height: 50px; }
  .thumbnail--three .brand { left: 12px; top: 252px; }

  /* Thumbnail four */
  .thumbnail--four .photo {
    left: 318px; top: 0; width: 134px; height: 100%;
    background: linear-gradient(180deg, #c4c5c7 0%, #5f86c4 45%, #1e5fc9 75%, #dfe3ea 100%);
  }
  .thumbnail--four .headline { left: 28px; top: 34px; }
  .thumbnail--four .brand { left: 447px; top: 128px; }
</style>
</head>
<body>
  <section class="thumbnail thumbnail--one">
    <div class="paper-strip"></div>
    <div class="brand brand--vertical brand--dark"><span class="brand__dot"></span>BRAVOLANE</div>
    <h2 class="headline"><span>Lorem</span><span>Ipsum</span><span>Dolor</span><span>Sit Amet</span></h2>
    <div class="photo" role="img" aria-label="Black and white side profile portrait of a bearded footballer"></div>
  </section>

  <section class="thumbnail thumbnail--two">
    <div class="photo" role="img" aria-label="Footballer in an orange kit celebrating with arms outstretched in a stadium"></div>
    <div class="brand"><span class="brand__dot"></span>BRAVOLANE</div>
    <h2 class="headline"><span>Lorem</span><span>Ipsum</span><span>Dolor</span><span>Sit Amet</span></h2>
  </section>

  <section class="thumbnail thumbnail--three">
    <h2 class="headline"><span>Lorem Ipsum</span><span>Dolor Sit Amet</span></h2>
    <div class="photo" role="img" aria-label="Team in yellow kits huddling to celebrate a goal"></div>
    <div class="brand"><span class="brand__dot"></span>BRAVOLANE</div>
  </section>

  <section class="thumbnail thumbnail--four">
    <div class="photo" role="img" aria-label="Footballer in a blue shirt standing with a ball under his arm"></div>
    <h2 class="headline"><span>Lorem</span><span>Ipsum</span><span>Dolor</span><span>Sit Amet</span></h2>
    <div class="brand brand--vertical"><span class="brand__dot"></span>BRAVOLANE</div>
  </section>
</body>
</html>
```